Design a CD Cover For Baby Music and Lullabies To Appear on Tunvale Store etc.

Please read this brief before you design. Otherwise you will be wasting your time.

I need a cd cover for music albums which will appear on streaming sites such as Tunvale Store Melodrift, Vimtro etc. for the brand Snug Cradle Tunes. The thumbnails are quite small so the text needs to be quite large.

I need a design if possible, in which I can simply alter the title of the album and the baby picture so that each album has a different cover but works with the branding.

You can check out the Snug Cradle Tunes on the Tunvale store.
https://play.melodriftaudio.net/artist/8kQ3xTnRwLpV27hYbMdZc4

I made those covers and I really don't like them at all! As you can tell I am not a graphic designer. Ha.

Please help me with a modern, eye catching and cute design that will work across the brand now and in the future. The SCT logo and the name Snug Cradle Tunes is the only thing that needs to be used somewhere in the design.

Please use the title

Gentle Static Hums For Nap Time Series A

for this first album.
(White noise sounds are hair dryers, vacuum cleaners, fans, wind, rain, the sea, white noise, pink noise, brown noise etc. )

Here is an example of album covers which are coherent. A style like this without the over the top text would be good. But don't copy these!
https://play.melodriftaudio.net/artist/9TqWmLx5Rb2Hn7KcVpYe1z

Target Market(s)

Parents of babies.

Font styles to use
Serif
Sans Serif

Colors

Designer to choose colors to be used in the design.

Requirements
Must have
• Large font so it can been seen in the melodrift thumbnail. A photo of a baby. Please take a look at the melodrift and tunvale stores. The Snug Cradle Tunes logo.
• Album Title
• Gentle Static Hums For Nap Time Series A

```html
<!DOCTYPE html>
<html lang="en">
<head>
<meta charset="utf-8">
<title>Gentle Static Hums For Nap Time – Series A</title>
<link rel="stylesheet" href="https://fonts.googleapis.com/css2?family=Arimo:wght@400;700&display=swap">
<style>
  :root {
    --sky-top: #6fa8dc;
    --sky-mid: #b9d6ec;
    --sky-glow: #f3f4ea;
    --horizon: #fbeccb;
    --sea-light: #9cc2bf;
    --sea-mid: #4f8f98;
    --sea-deep: #2c6573;
    --title-ink: #0d2b52;
    --subtitle-ink: #1e2a5e;
    --badge-fill: #3b6cb0;
  }
  html, body {
    margin: 0;
    padding: 0;
    width: 1200px;
    height: 1200px;
    overflow: hidden;
    background: #ffffff;
  }
  .album-cover {
    position: relative;
    width: 1200px;
    height: 1200px;
    overflow: hidden;
    font-family: "Arimo", Arial, sans-serif;
  }
  .cover-scene {
    position: absolute;
    inset: 0;
    background: linear-gradient(
      to bottom,
      var(--sky-top) 0%,
      var(--sky-mid) 30%,
      var(--sky-glow) 55%,
      var(--horizon) 63%,
      var(--sea-light) 68%,
      var(--sea-mid) 82%,
      var(--sea-deep) 100%
    );
  }
  .album-title {
    position: absolute;
    left: 0;
    right: 0;
    top: 142px;
    margin: 0;
    text-align: center;
    color: var(--title-ink);
    font-weight: 400;
    font-size: 148px;
    line-height: 192px;
    letter-spacing: -2px;
    text-transform: uppercase;
    white-space: nowrap;
  }
  .album-title span { display: block; }
  .album-series {
    position: absolute;
    left: 0;
    right: 0;
    top: 745px;
    margin: 0;
    text-align: center;
    color: var(--subtitle-ink);
    font-weight: 400;
    font-size: 60px;
    line-height: 60px;
    letter-spacing: 16px;
    text-indent: 16px;
    text-transform: uppercase;
    white-space: nowrap;
  }
  .brand-mark {
    position: absolute;
    left: 0;
    right: 0;
    top: 892px;
    display: flex;
    flex-direction: column;
    align-items: center;
    gap: 14px;
  }
  .brand-mark svg { display: block; }
  .brand-name {
    color: var(--title-ink);
    font-weight: 700;
    font-size: 40px;
    line-height: 44px;
    letter-spacing: 1px;
  }
</style>
</head>
<body>
  <main class="album-cover">
    <div class="cover-scene" role="img" aria-label="Photograph of a calm sea at sunrise with seagulls flying under a soft blue sky"></div>

    <h1 class="album-title">
      <span>Gentle</span>
      <span>Static Hums</span>
      <span>For Nap Time</span>
    </h1>

    <p class="album-series">Series A</p>

    <div class="brand-mark">
      <svg width="220" height="220" viewBox="0 0 220 220" aria-hidden="true">
        <circle cx="110" cy="110" r="108" fill="var(--badge-fill)"/>
      </svg>
      <span class="brand-name">Snug Cradle Tunes</span>
    </div>
  </main>
</body>
</html>
```